Business card design needed

I need a business card for my new business.
I make environmentally friendly candles from all natural premium ingredients.
The candles are hand-poured locally in Melbourne, Australia.
I also want my card to match my website www.velmoracandles-example.com.au (similar colours, font). Can add additional fonts to create more interest...
I want my design to reflect class and simplicity.
Target Market(s)
Target audience 25-50
The candles represent luxury but need to appeal to the environmentally conscious...
Needs to appeal to both men and women. A luxury gift a man would buy for his girlfriend or mother or for his home and for a woman it needs to represent quality...
Industry/Entity Type
Business
Contact Information for Business Card
Velmora Candles
Hand-Poured Eco Soy Candles
Lorena Whitcombe - Founder
0472 390 614
www.velmoracandles-example.com.au
Logo Text
VELMORA
Logo styles of interest
Wordmark Logo
Look and feel
Each slider illustrates characteristics of the customer's brand and the style your logo design should communicate.

```html
<!DOCTYPE html>
<html lang="en">
<head>
<meta charset="utf-8">
<title>Velmora Candles — Business Card</title>
<link rel="stylesheet" href="https://fonts.googleapis.com/css2?family=Zilla+Slab:ital,wght@0,300;0,400;0,700;1,300;1,400&display=swap">
<style>
  :root {
    --card-bg: #eeeeee;
    --card-bg-light: #f4f4f4;
    --ink: #5b5b5b;
    --candle-mid: #f1d66a;
    --candle-deep: #e9c13a;
  }
  html, body {
    margin: 0;
    padding: 0;
    overflow: hidden;
    background: #ffffff;
  }
  .card {
    position: relative;
    width: 1200px;
    height: 692px;
    overflow: hidden;
    background: linear-gradient(90deg, var(--card-bg) 0%, var(--card-bg-light) 60%, var(--card-bg-light) 100%);
    font-family: "Zilla Slab", serif;
    color: var(--ink);
  }
  .candle-photo {
    position: absolute;
    top: 0;
    right: 0;
    width: 520px;
    height: 692px;
    background:
      radial-gradient(ellipse 260px 90px at 380px 190px, rgba(247, 236, 170, 0.9), rgba(247, 236, 170, 0) 100%),
      radial-gradient(ellipse 220px 360px at 400px 480px, rgba(236, 196, 60, 0.85), rgba(236, 196, 60, 0) 100%),
      linear-gradient(90deg, rgba(244, 244, 244, 0) 0%, rgba(243, 234, 190, 0.6) 35%, var(--candle-mid) 70%, var(--candle-deep) 100%);
    background-repeat: no-repeat;
  }
  .card-content {
    position: absolute;
    left: 0;
    top: 0;
    width: 826px;
    height: 692px;
    text-align: center;
  }
  .card-content > * {
    position: absolute;
    left: 0;
    width: 826px;
    margin: 0;
  }
  .brand-name {
    top: 64px;
    font-weight: 300;
    font-size: 74px;
    line-height: 1;
    letter-spacing: 1px;
    white-space: nowrap;
  }
  .brand-rule {
    left: 297px !important;
    top: 165px;
    width: 236px !important;
    height: 3px;
    background: var(--ink);
  }
  .tagline {
    top: 192px;
    font-style: italic;
    font-weight: 300;
    font-size: 31px;
    line-height: 1.2;
    letter-spacing: 0.6px;
  }
  .person-name {
    top: 338px;
    font-weight: 700;
    font-size: 52px;
    line-height: 1.1;
    letter-spacing: 1.5px;
    white-space: nowrap;
  }
  .person-role {
    top: 404px;
    font-style: italic;
    font-weight: 400;
    font-size: 42px;
    line-height: 1.2;
    letter-spacing: 1px;
  }
  .contact {
    top: 548px;
    font-style: italic;
    font-weight: 300;
    line-height: 54px;
  }
  .contact span { display: block; white-space: nowrap; }
  .contact .phone { font-size: 43px; letter-spacing: 0.5px; }
  .contact .website { font-size: 36px; }
</style>
</head>
<body>
<div class="card">
  <div class="candle-photo" role="img" aria-label="Photograph of yellow pillar soy candles tied with twine"></div>
  <div class="card-content">
    <h1 class="brand-name">VELMORA CANDLES</h1>
    <div class="brand-rule"></div>
    <p class="tagline">Hand-Poured Eco Soy Candles</p>
    <p class="person-name">LORENA WHITCOMBE</p>
    <p class="person-role">Founder</p>
    <p class="contact">
      <span class="phone">0472.390.614</span>
      <span class="website">www.velmoracandles-example.com.au</span>
    </p>
  </div>
</div>
</body>
</html>
```